Professional, Attractive, Simple Website Needed!!

We completed the design for our logo.

We need a website built out around this.

Here are a couple samples of how we want ours formatted.

http://brvntapower.com

http://www.halvorbeam.com/lp/free-quote?LeadSource=Search%20Engine&ProgramName=webquery&experience=qual&language=en&type=brd&gclid=Xq7RTPwmEYKDLAvUHbsNQkfPZrTcGwnJuoVbXeLqHmRYdAsWtPkMcNfBYgzTrUoQJhEdWvKpYaLsZbCmNDgQwTxAoKpXbT_qkR

http://morvalo.co

Reason: Extending this deadline due to our delay in providing designers with content for each page. This is coming in next 24 hours.

Reason: Due to scheduling conflicts and extended travel delays related to Puerto Rico, the deadline has been extended. Your patience is greatly appreciated.

Reason: Travel and scheduling conflicts have made it impossible to give this project the thorough review it deserves, therefore I am extending the deadline. Thank you for your patience!

Target Market(s)

Home Owners who earn 60k + household annually

Industry/Entity Type

It Professional

Coding

Coded - Design and coding required

Number of Pages Required

5+ page

Font styles to use
Serif

Colors
34a7d8
9bcb3c

Requirements
Must have
• Simple
• Lead form Entry (Ability for visitor to enter Name, number and address for a quote)
• Sleek Design
• Professional
• Testimonials
• Use color Scheme of Design Logo Attached
Nice to have
• Video when site starts
• Like this
• https://www.vidmarrow.com/watch?v=qT8mRpXw2Ka&feature=vidm.ro
Should not have
• Should not include Commercial solar
• Should not include wind power

```html
<!DOCTYPE html>
<html lang="en">
<head>
<meta charset="utf-8">
<title>Sunward Home Energy – Solar savings start here</title>
<link href="https://fonts.googleapis.com/css2?family=Poppins:wght@400;500;600&family=Open+Sans:wght@400;600&display=swap" rel="stylesheet">
<style>
:root{
  --blue:#0b84cf;
  --blue-deep:#066aa8;
  --green:#9bcb3c;
  --sky-top:#d6eef5;
  --sky-bottom:#eef8fb;
  --ink:#1d1d1d;
  --soft-bg:#f4f4f4;
  --white:#ffffff;
}
*{box-sizing:border-box;margin:0;padding:0}
html,body{width:1200px;height:3130px;overflow:hidden}
body{position:relative;background:var(--white);font-family:"Open Sans",Arial,sans-serif;color:var(--ink)}
.abs{position:absolute}
h1,h2,h3,.poppins{font-family:"Poppins",Arial,sans-serif}

/* header & hero */
.hero{left:0;top:0;width:1200px;height:620px;background:linear-gradient(180deg,var(--sky-top),var(--sky-bottom));overflow:hidden}
.brand{left:96px;top:30px;display:flex;align-items:center;gap:10px;font-family:"Poppins",sans-serif;font-weight:600;font-size:17px;color:var(--blue)}
.brand-dot{width:40px;height:40px;border-radius:50%;border:3px solid var(--blue)}
.nav{right:80px;top:64px;display:flex;gap:28px;font-family:"Poppins",sans-serif;font-size:12px;font-weight:500;color:#333;text-transform:uppercase;align-items:center}
.nav .home{width:13px;height:12px}
.hero-title{left:86px;top:252px;font-size:38px;font-weight:500;color:#111}
.hero-text{left:86px;top:306px;width:420px;font-size:13px;line-height:24px;color:#333}
.play{left:0;top:371px;width:196px;height:63px;background:var(--blue);border-radius:0 4px 4px 0;color:#fff;display:flex;align-items:center;padding-left:50px;gap:16px;z-index:2}
.play small{display:block;font-size:8px;opacity:.85}
.play b{font-family:"Poppins",sans-serif;font-weight:500;font-size:15px}
.hero-scene{left:0;top:170px;width:1200px;height:450px;
  background:
    radial-gradient(ellipse 300px 90px at 250px 405px,rgba(150,160,70,.55),rgba(150,160,70,0) 100%),
    radial-gradient(ellipse 320px 200px at 905px 360px,rgba(236,178,70,.45),rgba(236,178,70,0) 100%),
    radial-gradient(ellipse 420px 180px at 900px 150px,rgba(255,255,255,.9),rgba(255,255,255,0) 100%);}
.ground{left:0;top:608px;width:1200px;height:12px;background:var(--green)}

/* steps */
.steps{left:0;top:612px;width:1200px;height:573px;background:var(--soft-bg)}
.steps svg.wave{position:absolute;left:0;top:0}
.steps-title{left:0;top:125px;width:1200px;text-align:center;font-size:34px;font-weight:500;color:#fff;letter-spacing:.5px}
.steps-text{left:200px;top:176px;width:800px;text-align:center;font-size:12.5px;line-height:22px;color:#fff}
.step-icon{width:86px;height:86px;border-radius:50%;background:#fff;box-shadow:0 6px 16px rgba(0,0,0,.12);display:flex;align-items:center;justify-content:center}
.step-label{display:flex;align-items:center;gap:12px;font-size:13px;line-height:18px;color:#222}
.step-num{width:34px;height:34px;border-radius:50%;background:var(--blue);color:#fff;font-size:12px;display:flex;align-items:center;justify-content:center;flex:none}

/* stories */
.section-title{font-size:29px;font-weight:500;color:#111;letter-spacing:.5px}
.avatar{width:46px;height:46px;border-radius:50%;background:linear-gradient(135deg,#8a96a6,#3d4756)}
.quote{left:168px;top:1450px;width:540px;font-family:"Poppins",sans-serif;font-size:19px;line-height:29px;color:#222;padding-left:41px}
.quote-mark{left:168px;top:1442px;font-family:"Poppins",sans-serif;font-size:44px;color:var(--green);font-weight:600}
.story-body{left:209px;top:1522px;width:490px;font-size:12px;line-height:21px;color:#666}
.story-by{left:209px;top:1614px;font-size:11px;color:#999}
.story-by b{color:var(--blue);font-weight:400}
.arrow-btn{width:34px;height:34px;border-radius:50%;display:flex;align-items:center;justify-content:center}

.quote-form{left:781px;top:1311px;width:329px;height:426px;background:var(--blue);border-radius:4px;box-shadow:0 18px 36px rgba(0,0,0,.18);padding:56px 34px 0;color:#fff}
.quote-form h3{font-weight:500;font-size:24px;margin-bottom:22px}
.quote-form label{display:block;font-size:11px;margin-bottom:8px}
.field{height:42px;background:#fff;border-radius:3px;font-size:11px;color:#888;display:flex;align-items:center;padding-left:18px;margin-bottom:16px;gap:8px}
.submit{height:42px;background:var(--green);border-radius:3px;color:#fff;font-size:11px;display:flex;align-items:center;justify-content:center;text-transform:uppercase;margin-top:6px}

/* news */
.card{top:1937px;width:325px;height:425px;background:#fff;box-shadow:0 10px 26px rgba(0,0,0,.1)}
.card .photo{height:240px}
.card .meta{margin:26px 28px 0;font-size:11px;color:#444}
.card .meta span{color:#999}
.card h3{margin:14px 28px 0;font-size:19px;font-weight:400;line-height:28px;color:#222}
.tag{display:inline-block;margin:14px 28px 0;padding:4px 18px;border-radius:12px;font-size:8px;text-transform:uppercase}
.tag.blog{background:#e3f1fb;color:var(--blue);border:1px solid #bcdcf2}
.tag.news{background:#f1f8e4;color:#8bb834;border:1px solid #d6eaad}

/* cta */
.cta{left:88px;top:2456px;width:1022px;height:107px;background:linear-gradient(90deg,#9fcc42,#b2d65f 50%,#9fcc42);border-radius:3px}
.cta-text{left:60px;top:30px;font-family:"Poppins",sans-serif;font-size:28px;color:#fff;letter-spacing:.5px}
.cta-btn{right:0;top:25px;width:194px;height:63px;background:var(--blue);border-radius:3px;color:#fff;display:flex;align-items:center;gap:16px;padding-left:32px}
.cta-btn small{display:block;font-size:8px;opacity:.85}
.cta-btn b{font-family:"Poppins",sans-serif;font-weight:500;font-size:15px}

/* footer */
.footer{left:0;top:2634px;width:1200px;height:496px;background:linear-gradient(180deg,#3f9fdc 0,var(--blue) 130px)}
.footer-logo{left:80px;top:2852px;width:270px;display:flex;flex-direction:column;align-items:center;gap:12px;font-family:"Poppins",sans-serif;font-size:22px;color:#fff;white-space:nowrap}
.footer-logo .ring{width:78px;height:78px;border-radius:50%;border:4px solid #fff}
.f-head{font-family:"Poppins",sans-serif;font-weight:600;font-size:15px;color:#fff}
.links{list-style:none;font-size:11px;color:#fff}
.links li{height:27px}
.links li::before{content:"›";margin-right:10px}
.f-text{font-size:11px;line-height:19px;color:#fff}
.f-input{height:40px;background:#fff;border-radius:2px;font-size:11px;color:#888;display:flex;align-items:center;padding-left:14px}
.f-btn{height:40px;background:var(--green);border-radius:2px;color:#fff;font-size:11px;display:flex;align-items:center;justify-content:center;text-transform:uppercase}
.social{display:flex;align-items:center;gap:14px;font-size:11px;color:#fff;height:33px}
.social i{width:24px;height:24px;border-radius:50%;background:#1d5f9a;display:block}
.social i.red{background:#dd4b39}
.copyright{left:0;top:3085px;width:1200px;height:45px;background:var(--blue-deep);color:#fff;font-size:10px;text-align:center;line-height:45px}
.to-top{left:1127px;top:3068px;width:34px;height:34px;border-radius:50%;background:var(--green);display:flex;align-items:center;justify-content:center}
</style>
</head>
<body>

<section class="hero abs">
  <div class="hero-scene abs" role="img" aria-label="Illustrated row of green trees beside colourful town buildings under soft clouds"></div>
  <div class="ground abs"></div>
  <div class="brand abs"><span class="brand-dot"></span>Sunward Home Energy</div>
  <nav class="nav abs">
    <svg class="home" viewBox="0 0 13 12"><path d="M6.5 0 13 6h-2v6H8V8H5v4H2V6H0z" fill="#0b84cf"/></svg>
    <span>Why</span><span>Partnerships</span><span>Foundation</span><span>Blog</span><span>FAQ</span><span>Contact Us</span>
  </nav>
  <h1 class="hero-title abs">Solar savings start here.</h1>
  <p class="hero-text abs">Lorem ipsum dolor sit amet, consectetuer adipiscing elit aenean commodo ligula eget dolor aenean massa.</p>
  <div class="play abs">
    <svg width="20" height="22" viewBox="0 0 20 22"><path d="M0 0 20 11 0 22z" fill="#fff"/></svg>
    <div><small>Sunward Home Energy</small><b>Play Video</b></div>
  </div>
</section>

<section class="steps abs">
  <svg class="wave" width="1200" height="400" viewBox="0 0 1200 400">
    <path d="M0 0H1200V212C1140 214 1080 250 1020 254 960 258 930 240 880 254 820 270 800 340 740 340 660 340 600 268 520 264 440 260 380 310 300 340 220 370 100 380 0 370Z" fill="var(--green)"/>
  </svg>
  <h2 class="steps-title abs">4 EASY STEPS TO GOING SOLAR</h2>
  <p class="steps-text abs">Lorem ipsum dolor sit amet, consectetuer adipiscing elit. Aenean commodo ligula eget dolor aenean massa. Cum sociis natoque penatibus et magnis dis parturient montes nascetur ridiculus mus donec quam felis ultricies nec.</p>

  <div class="step-icon abs" style="left:168px;top:318px">
    <svg width="38" height="38" viewBox="0 0 38 38" fill="none" stroke="#222" stroke-width="2.5"><path d="M6 22v-4a13 13 0 0 1 26 0v4"/><rect x="4" y="20" width="7" height="10" rx="2" fill="#222"/><rect x="27" y="20" width="7" height="10" rx="2" fill="#222"/><circle cx="19" cy="21" r="7"/></svg>
  </div>
  <div class="step-icon abs" style="left:429px;top:255px">
    <svg width="40" height="38" viewBox="0 0 40 38" fill="none" stroke="#222" stroke-width="2.2"><path d="M6 10h28l4 16H2z"/><path d="M14 10l-2 16M26 10l2 16M4 18h32"/><path d="M20 26v8M12 34h16"/></svg>
  </div>
  <div class="step-icon abs" style="left:677px;top:326px">
    <svg width="34" height="34" viewBox="0 0 34 34" fill="none" stroke="#222" stroke-width="2.5"><rect x="3" y="6" width="28" height="25" rx="2"/><path d="M3 13h28M10 2v7M24 2v7"/><path d="M9 18h3M16 18h3M23 18h3M9 24h3M16 24h3M23 24h3"/></svg>
  </div>
  <div class="step-icon abs" style="left:930px;top:301px">
    <span class="poppins" style="font-size:34px;font-weight:500;color:#222">$</span>
  </div>

  <div class="step-label abs" style="left:144px;top:431px"><span class="step-num">1</span>Speak to a<br>solar consultant</div>
  <div class="step-label abs" style="left:388px;top:385px"><span class="step-num">2</span>We'll design your<br>solar panel system</div>
  <div class="step-label abs" style="left:647px;top:444px"><span class="step-num">3</span>Schedule your<br>1 day install</div>
  <div class="step-label abs" style="left:889px;top:408px"><span class="step-num">4</span>Start saving on your<br>electricity bill</div>
</section>

<h2 class="section-title poppins abs" style="left:88px;top:1372px">SUCCESS STORIES</h2>
<div class="avatar abs" style="left:87px;top:1438px" role="img" aria-label="Customer portrait"></div>
<div class="avatar abs" style="left:87px;top:1511px" role="img" aria-label="Customer portrait"></div>
<div class="avatar abs" style="left:87px;top:1574px" role="img" aria-label="Customer portrait"></div>
<div class="avatar abs" style="left:87px;top:1636px" role="img" aria-label="Customer portrait"></div>
<span class="quote-mark abs">“</span>
<p class="quote abs">Lorem ipsum dolor sit amet, consectetuer adipiscing elit. Aenean commodo ligula eget dolor.</p>
<p class="story-body abs">Lorem ipsum dolor sit amet, consectetuer adipiscing elit. Aenean commodo ligula eget dolor. Aenean massa. Cum sociis natoque penatibus et magnis dis parturient montes, nascetur ridiculus mus. Donec quam felis, ultricies nec, pellentesque eu, pretium quis,Lorem ipsum dolor sit amet, consectetuer .</p>
<p class="story-by abs"><b>John Smith</b> • CEO MARKETING</p>
<div class="arrow-btn abs" style="left:204px;top:1651px;background:#fff;box-shadow:0 2px 8px rgba(0,0,0,.15)">
  <svg width="8" height="12" viewBox="0 0 8 12"><path d="M7 1 2 6l5 5" fill="none" stroke="#888" stroke-width="2"/></svg>
</div>
<div class="arrow-btn abs" style="left:246px;top:1651px;background:var(--blue)">
  <svg width="8" height="12" viewBox="0 0 8 12"><path d="M1 1l5 5-5 5" fill="none" stroke="#fff" stroke-width="2"/></svg>
</div>

<form class="quote-form abs">
  <h3 class="poppins">Request a Quote</h3>
  <label>Name :</label><div class="field">Enter your name</div>
  <label>Number :</label><div class="field">Enter your number</div>
  <label>Address :</label>
  <div class="field"><svg width="10" height="13" viewBox="0 0 10 13"><path d="M5 0a5 5 0 0 0-5 5c0 4 5 8 5 8s5-4 5-8a5 5 0 0 0-5-5zm0 7a2 2 0 1 1 0-4 2 2 0 0 1 0 4z" fill="#666"/></svg>Enter your Address</div>
  <div class="submit">Request Now</div>
</form>

<h2 class="section-title poppins abs" style="left:0;width:1200px;text-align:center;top:1860px">STAY UP TO DATE</h2>
<p class="abs" style="left:0;width:1200px;text-align:center;top:1896px;font-size:11px;color:#777">Recent News</p>

<article class="card abs" style="left:86px">
  <div class="photo" role="img" aria-label="Sunlit tree over a green field" style="background:linear-gradient(160deg,#6b8f3a,#c9dc8a 45%,#3f6a22)"></div>
  <p class="meta">by Johnson D. <span>• 17 hours ago</span></p>
  <h3>Blog 1 heading: Some news heading goes here...</h3>
  <span class="tag blog">Blog</span>
</article>
<article class="card abs" style="left:434px">
  <div class="photo" role="img" aria-label="Smiling couple outdoors" style="background:linear-gradient(160deg,#cfc6a8,#8ea6b8 55%,#b59a7a)"></div>
  <p class="meta">by Sara Doe <span>• 18 hours ago</span></p>
  <h3>News 2 heading: Some news heading goes here...</h3>
  <span class="tag news">News</span>
</article>
<article class="card abs" style="left:785px">
  <div class="photo" role="img" aria-label="Woman watching a bright sunset" style="background:linear-gradient(160deg,#f6c46a,#d9713a 45%,#4a3326)"></div>
  <p class="meta">by Mark Johnson <span>• 17 hours ago</span></p>
  <h3>Blog 3 heading: Some news heading goes here...</h3>
  <span class="tag blog">Blog</span>
</article>

<div class="cta abs" role="img" aria-label="Green meadow with a lone tree">
  <span class="cta-text abs">LET US SAVE YOU SOME $$$</span>
  <div class="cta-btn abs">
    <svg width="26" height="16" viewBox="0 0 26 16"><path d="M0 8h24M17 1l7 7-7 7" fill="none" stroke="#fff" stroke-width="2"/></svg>
    <div><small>Contact Us</small><b>Get a Quote</b></div>
  </div>
</div>

<footer class="footer abs" role="img" aria-label="Blue city skyline silhouette along the top edge"></footer>
<div class="footer-logo abs"><span class="ring"></span>Sunward Home Energy</div>

<h4 class="f-head abs" style="left:403px;top:2828px">USEFUL LINKS</h4>
<ul class="links abs" style="left:403px;top:2866px">
  <li>WHY</li><li>PARTNERSHIPS</li><li>FOUNDATION</li><li>BLOG</li><li>FAQ</li><li>CONTACT US</li>
</ul>

<h4 class="f-head abs" style="left:614px;top:2828px">LOCK IN YOUR RATE</h4>
<p class="f-text abs" style="left:614px;top:2862px;width:250px">No more rate hikes. We'll let you lock in your rate for 20 years.</p>
<div class="f-input abs" style="left:614px;top:2913px;width:242px">Zip Code</div>
<div class="f-btn abs" style="left:614px;top:2957px;width:242px">Calculate your savings</div>

<h4 class="f-head abs" style="left:925px;top:2828px">FOLLOW US</h4>
<div class="abs" style="left:920px;top:2858px">
  <div class="social"><i></i>Friendwall</div>
  <div class="social"><i></i>Chirpline</div>
  <div class="social"><i class="red"></i>Circleplus</div>
  <div class="social"><i></i>Workfolio</div>
</div>

<div class="copyright abs">Copyright © Sunward Home Energy 2017. ALL RIGHTS RESERVED</div>
<div class="to-top abs">
  <svg width="12" height="8" viewBox="0 0 12 8"><path d="M1 7l5-5 5 5" fill="none" stroke="#fff" stroke-width="2"/></svg>
</div>

</body>
</html>
```